Retail Jewelry Business Card Design Project

We are in need of a new business card design for a retail jewelry store. This store is in the business of fine jewelry including but not specific to bridal jewelry, diamonds, designer jewelry and watches.

This store has been in business for 20 years but continues to strive for a modern professional appeal. The main colors use for this business are a royal blue, white and silver.

Target Market(s)

Target market is ages 18-50

Industry/Entity Type

Jewelry

Requirements
Must have
• Sales Person Name
Sales Person Email Address

Store Address
Store Phone
Website

Standard business card size. No odd shapes or sizes.
Nice to have
• Overall modern feel for card.

We have thought that a design with a nice feature of the logo on the back of the card would be nice but open to ideas.
Should not have
• No specific images of jewelry should be used.

```html
<!DOCTYPE html>
<html lang="en">
<head>
<meta charset="utf-8">
<title>Aldren Hale Fine Jewelry – Business Card</title>
<link rel="stylesheet" href="https://fonts.googleapis.com/css2?family=Tinos&display=swap">
<style>
  :root {
    --page-bg: #ececec;
    --silver-light: #f4f4f4;
    --silver-mid: #c9c9c9;
    --silver-dark: #9a9a9a;
    --royal-blue: #2b2a85;
    --ink-grey: #3c3c46;
    --paper: #ffffff;
  }
  * { box-sizing: border-box; margin: 0; padding: 0; }
  html, body {
    width: 1136px;
    height: 1200px;
    overflow: hidden;
    background: var(--page-bg);
    font-family: "Tinos", "Times New Roman", serif;
  }
  .card {
    position: absolute;
    left: 118px;
    width: 900px;
    height: 514px;
    overflow: hidden;
    box-shadow: 0 6px 18px rgba(0,0,0,0.18);
  }
  .card--front { top: 57px; }
  .card--back  { top: 628px; }

  .brushed-silver {
    position: absolute;
    inset: 0;
    background:
      linear-gradient(180deg,
        var(--silver-dark) 0%,
        var(--silver-mid) 18%,
        var(--silver-light) 38%,
        var(--silver-mid) 55%,
        var(--silver-light) 72%,
        var(--silver-mid) 88%,
        var(--silver-dark) 100%);
  }

  .front-name {
    position: absolute;
    left: 0; right: 0;
    top: 222px;
    text-align: center;
    font-size: 50px;
    color: var(--paper);
    letter-spacing: 1px;
  }

  .back-panel {
    position: absolute;
    left: 22px;
    top: 22px;
    width: 728px;
    height: 470px;
    background: var(--paper);
  }
  .back-name {
    position: absolute;
    left: 48px;
    top: 86px;
    font-size: 34px;
    color: var(--royal-blue);
  }
  .contact {
    position: absolute;
    left: 376px;
    top: 216px;
    font-size: 18px;
    line-height: 30px;
    font-style: normal;
  }
  .contact__person { color: var(--royal-blue); }
  .contact__store { margin-top: 22px; color: var(--ink-grey); }
</style>
</head>
<body>
  <section class="card card--front">
    <div class="brushed-silver" role="img" aria-label="Brushed silver metal texture"></div>
    <p class="front-name">Aldren Hale Fine Jewelry</p>
  </section>

  <section class="card card--back">
    <div class="brushed-silver" role="img" aria-label="Brushed silver metal texture"></div>
    <div class="back-panel">
      <p class="back-name">Aldren Hale Fine Jewelry</p>
      <address class="contact">
        <div class="contact__person">
          <div>Aldren Hale Marsden</div>
          <div>aldren@aldrenhalejewelry.com</div>
        </div>
        <div class="contact__store">
          <div>Aldren Hale Fine</div>
          <div>2210 Wexford Avenue</div>
          <div>Bay Harbor, FL 32490</div>
          <div>www.aldrenhalejewelry.com</div>
        </div>
      </address>
    </div>
  </section>
</body>
</html>
```